FlipCrane is a crypto-arbitrage tool that finds arbitrages between and within exchanges.A logo for the websiteA designer will need to design main page which will describe the project.A subscription page which will have subscription packages. A client portal page where client can set filter types, payment options etc...A Solutions page which will have the actual solutions which flipCrane will calculate. Other pages that have to do with login and subscribing. We need all this to be done as a project with actual color numbers high quality images. ETC... We have attached the current Mock up but designer should have their own input and make it better.
Updates
Project is large and people need time to get it done, please extend by 3 weeks
Need more time to get the project finished right
Target Market(s)
Crypto Traders that are looking to make more money trading
Industry/Entity Type
Finance
Coding
Coded - Design and coding required
Number of Pages Required
5+ page
Colors
Designer to choose colors to be used in the design.
Requirements
Nice to have
- Good animations

```html
<!DOCTYPE html>
<html lang="en">
<head>
<meta charset="utf-8">
<title>FlipCrane — Crypto Arbitrage</title>
<link rel="stylesheet" href="https://fonts.googleapis.com/css2?family=Montserrat:wght@400;500;600;700&family=Open+Sans:wght@400;600;700&display=swap">
<style>
:root{
  --yellow:#f8d90f;
  --ink:#1c1e21;
  --grey:#6b6f75;
  --line:#dcdcdc;
  --white:#ffffff;
}
*{box-sizing:border-box;margin:0;padding:0}
html,body{width:1200px;height:4417px;overflow:hidden}
body{font-family:"Open Sans",Arial,sans-serif;color:var(--ink);background:var(--white);font-size:14px;line-height:1.6}
h1,h2,h3,h4{font-family:"Montserrat",Arial,sans-serif}
.section{position:relative;width:1200px;overflow:hidden}
.photo{position:absolute;inset:0}
.shade{position:absolute;inset:0;background:rgba(20,22,26,.72)}
.inner{position:relative;z-index:1}
.btn{display:inline-block;font-family:"Montserrat",sans-serif;font-weight:700;font-size:13px;letter-spacing:.5px;padding:12px 26px;border-radius:30px;background:var(--yellow);color:var(--ink);text-decoration:none}
.btn-outline{background:transparent;border:2px solid var(--white);color:var(--white)}
.title-center{text-align:center;font-size:34px;font-weight:600}
.title-center::after,.title-left::after{content:"";display:block;width:70px;height:4px;background:var(--yellow);margin:10px auto 0}
.title-left::after{margin:10px 0 0}

/* hero */
.hero{height:552px;color:var(--white)}
.hero .photo{background:linear-gradient(120deg,#5a6470 0%,#8a939c 45%,#4a525b 100%)}
.hero .shade{background:linear-gradient(180deg,rgba(25,28,32,.55),rgba(25,28,32,.8))}
.nav{display:flex;align-items:center;height:80px;padding:0 45px}
.brand{display:flex;align-items:center;gap:10px;font-family:"Montserrat",sans-serif;font-weight:700;font-size:18px;color:var(--white)}
.brand-mark{width:34px;height:34px;background:var(--yellow)}
.nav-links{display:flex;gap:30px;margin-left:160px;font-size:13px;font-weight:600}
.nav-login{margin-left:auto;border-radius:20px;padding:6px 18px;font-size:13px;font-weight:700;background:var(--white);color:var(--ink)}
.hero h1{font-size:35px;font-weight:500;line-height:1.3;width:1020px;margin:50px 0 0 45px}
.hero-actions{margin:34px 0 0 45px;display:flex;gap:14px}
.profits{margin:80px 0 0 45px}
.profits h4{font-size:19px;font-weight:700}
.profit-list{display:flex;gap:16px;margin-top:14px}
.profit-pill{display:flex;align-items:center;gap:8px;background:rgba(0,0,0,.55);border-radius:20px;padding:8px 18px;font-size:13px;font-weight:700}
.profit-pill::before{content:"";width:10px;height:10px;border-radius:50%;background:var(--yellow)}

/* why us */
.why{height:596px;background:var(--white)}
.why .title-center{padding-top:60px}
.why .lead{width:720px;margin:22px auto 0;text-align:center;color:var(--grey);font-size:14px}
.features{display:flex;justify-content:center;gap:40px;margin-top:100px}
.feature{width:210px;text-align:center}
.feature svg{width:48px;height:48px}
.feature h3{font-size:18px;font-weight:600;margin:12px 0 8px}
.feature p{font-size:12px;color:var(--grey);line-height:1.5}

/* what is */
.what{height:666px;color:var(--white)}
.what .photo{background:linear-gradient(135deg,#3b4149,#60676f 50%,#30353b)}
.what .shade{background:rgba(22,24,28,.75)}
.what .inner{padding:60px 155px 0}
.what h2{font-size:30px;font-weight:600}
.what p{font-size:13.5px;margin-top:18px;line-height:1.65}
.what .strong{font-weight:700;font-size:16px;width:620px}
.what .why-right{text-align:right;margin-top:40px}
.what .why-right h2::after{margin:10px 0 0 auto}

/* subscribe */
.subscribe{height:405px;background:var(--white);text-align:center}
.subscribe .title-center{padding-top:95px}
.subscribe p{width:820px;margin:22px auto 0;color:var(--grey);font-size:13.5px}
.subscribe .btn{margin-top:26px}

/* how */
.how{height:515px;color:var(--white)}
.how .photo{background:linear-gradient(125deg,#4c535b,#7b838b 55%,#3a3f45)}
.how .title-center{padding-top:36px}
.how .intro{width:880px;margin:26px auto 0;font-size:13px;font-style:italic}
.steps{display:flex;justify-content:center;gap:28px;margin-top:36px}
.step{width:205px}
.step svg{width:30px;height:30px}
.step h3{font-size:16px;font-weight:700;margin:6px 0}
.step p{font-size:12px;line-height:1.5}
.step .more{display:block;margin-top:6px;font-weight:700;font-size:12px}
.how .cta{text-align:center;margin-top:34px}

/* promote */
.promote{height:563px;background:var(--white)}
.promote .title-center{padding-top:62px}
.cards{display:flex;justify-content:center;gap:75px;margin-top:36px}
.card{width:235px;text-align:center}
.card-img{height:232px}
.card h3{font-size:16px;font-weight:600;margin-top:12px}
.card p{font-size:12px;color:var(--grey);line-height:1.45;margin-top:4px}
.card .btn{margin-top:12px;padding:8px 20px;font-size:12px}

/* split */
.split{height:497px;display:flex}
.half{position:relative;width:600px;height:497px;color:var(--white)}
.half .photo{background:linear-gradient(135deg,#3d4248,#6a7178)}
.half.right .photo{background:linear-gradient(135deg,#565d65,#2e3237)}
.half .shade{background:rgba(20,22,26,.7)}
.half .inner{padding:50px 50px 0 175px}
.half.right .inner{padding:50px 60px 0 10px}
.half h2{font-size:30px;font-weight:600}
.bullets{list-style:none;margin-top:26px}
.bullets li{position:relative;padding-left:22px;font-size:12.5px;margin-bottom:14px;line-height:1.45}
.bullets li::before{content:"";position:absolute;left:0;top:6px;width:8px;height:8px;background:var(--yellow)}
.half.right p{font-size:12.5px;margin-top:24px;line-height:1.5}

/* email & faq */
.info{height:460px;display:flex;padding:40px 0 0 175px;gap:40px}
.email{width:390px}
.email h2,.faq h2{font-size:27px;font-weight:600;white-space:nowrap}
.email p{font-size:12.5px;color:var(--grey);margin-top:18px}
.email-img{width:360px;height:150px;margin-top:22px}
.faq{width:450px}
.faq-list{list-style:none;margin-top:24px}
.faq-list li{display:flex;justify-content:space-between;align-items:center;border:1px solid var(--line);padding:11px 14px;font-size:13px;margin-bottom:12px}
.faq-list li.open{border:none}
.faq-dot{width:18px;height:18px;border-radius:50%;border:2px solid #2b3a55;flex:none}

/* footer */
.footer{height:162px;background:var(--ink);color:#c9c9c9;display:flex;padding:26px 0 0 175px;gap:90px;font-size:12px}
.footer h4{color:var(--yellow);font-size:13px;font-weight:700;margin-bottom:6px}
.footer ul{list-style:none;line-height:1.8}
.footer .meta{margin-left:20px;line-height:1.8}
</style>
</head>
<body>

<header class="section hero">
  <div class="photo" role="img" aria-label="Open-plan office with people working at desks"></div>
  <div class="shade"></div>
  <div class="inner">
    <nav class="nav">
      <div class="brand"><span class="brand-mark"></span>FlipCrane</div>
      <div class="nav-links">
        <span>Why us?</span><span>What is FlipCrane?</span><span>Subscribe for free</span><span>How it works</span><span>FAQ</span>
      </div>
      <span class="nav-login">Login / Sign Up</span>
    </nav>
    <h1>FlipCrane is an advanced piece of technology that is built for you to take advantage of current crypto markets.</h1>
    <div class="hero-actions">
      <a class="btn">SUBSCRIBE FOR FREE</a>
      <a class="btn btn-outline">LEARN MORE</a>
    </div>
    <div class="profits">
      <h4>Current Potential Profits</h4>
      <div class="profit-list">
        <span class="profit-pill">3 STEPS 34.60€</span>
        <span class="profit-pill">3 STEPS 245.72€</span>
        <span class="profit-pill">3 STEPS 712.30€</span>
        <span class="profit-pill">5 STEPS 4.56€</span>
      </div>
    </div>
  </div>
</header>

<section class="section why">
  <h2 class="title-center">Why us?</h2>
  <p class="lead">We help you make trades better and easier, taking out all the guess work. Whether you have no experience or are experienced already, we calculate the solutions for you that only commission can do.</p>
  <div class="features">
    <div class="feature">
      <svg viewBox="0 0 48 48" fill="none" stroke="#1c1e21" stroke-width="2.5"><circle cx="20" cy="20" r="12"/><line x1="29" y1="29" x2="42" y2="42"/></svg>
      <h3>Transparency</h3>
      <p>24 hour trading operations. Real time settlement. All transaction records available upon request.</p>
    </div>
    <div class="feature">
      <svg viewBox="0 0 48 48" fill="#1c1e21"><rect x="6" y="28" width="8" height="14"/><rect x="20" y="18" width="8" height="24"/><rect x="34" y="8" width="8" height="34"/></svg>
      <h3>High Preformance</h3>
      <p>Institutional grade trading architecture. Advanced technology design. API capabilities.</p>
    </div>
    <div class="feature">
      <svg viewBox="0 0 48 48" fill="none" stroke="#1c1e21" stroke-width="2.5"><path d="M24 5 L40 11 V23 C40 33 33 40 24 43 C15 40 8 33 8 23 V11 Z"/><polyline points="17,24 22,29 31,19"/></svg>
      <h3>Security</h3>
      <p>Multi-level firewall and segmentation. Real-time system monitoring. Multi-signature environment.</p>
    </div>
    <div class="feature">
      <svg viewBox="0 0 48 48" fill="none" stroke="#1c1e21" stroke-width="2.5"><circle cx="24" cy="16" r="8"/><path d="M8 42 C8 32 15 27 24 27 C33 27 40 32 40 42"/></svg>
      <h3>Experience</h3>
      <p>Years of knowledge of crypto market structure. In-depth R&amp;D experience in arbitrage trading. Proven track record.</p>
    </div>
  </div>
</section>

<section class="section what">
  <div class="photo" role="img" aria-label="Office workspace with monitors"></div>
  <div class="shade"></div>
  <div class="inner">
    <h2 class="title-left">What Is FlipCrane?</h2>
    <p>FlipCrane compares cryptocurrency prices across various exchanges to find profitable trading solutions. The results are compiled and displayed to the user, showing where he/she can buy LOW and sell HIGH with great profit. Trading solutions are calculated in several ways. From simple 2 step arbitrage to more complicated solutions with 5 steps. FlipCrane includes all necessary information to make sure that each solution is actually profitable, such as checking for transfer availability, average duration of coin transfers, and order books. FlipCrane has a built in advanced transaction profitability calculator that includes all of the commissions and transaction costs for each trading solution. FlipCrane is an advanced piece of technology that is built for you to take advantage of current markets.</p>
    <p class="strong">For more professional traders we have API solutions that feed trading solutions straight to your trading BOT.</p>
    <div class="why-right">
      <h2 class="title-left">Why FlipCrane?</h2>
    </div>
    <p>FlipCrane's software has been designed by professionals and has a proven track record for over 3 years. This solutions engine is being used by investment firms for other capital markets, such as FX, Equities and Futures. However, crypto markets have a lot of untapped potential and we want to show those trading solutions to you.<br>We provide solutions that are real, quicker and deeper than triangular arbitrage. Our tool is versatile and fast. Our code looks at a large set of data and provides the best solution every 2 minutes, looking through more than 100K permutations. No one else even comes close to our speed and our capabilities.</p>
  </div>
</section>

<section class="section subscribe">
  <h2 class="title-center">Subscribe for Free</h2>
  <p>Subscribe now for free and see trading solutions from the previous hour. See if you like our services, however the data will be delayed.<br>We will also email you about best trading solutions from the previous hour every hour to keep you in the loop.</p>
  <a class="btn">SUBSCRIBE NOW</a>
</section>

<section class="section how">
  <div class="photo" role="img" aria-label="Team working in a bright office"></div>
  <div class="shade"></div>
  <div class="inner">
    <h2 class="title-center">How It Works?</h2>
    <p class="intro">FlipCrane automatically scans dozens of exchanges and displays trading solutions according to your preferences and filters, allowing you where to buy LOW and sell HIGH with good return on your investment.</p>
    <div class="steps">
      <div class="step">
        <svg viewBox="0 0 30 30" fill="none" stroke="#fff" stroke-width="2"><polyline points="3,24 11,15 17,20 27,7"/></svg>
        <h3>Profit</h3>
        <p>FlipCrane shows you where to buy and sell with a large profit.</p>
        <span class="more">Read more &gt;&gt;</span>
      </div>
      <div class="step">
        <svg viewBox="0 0 30 30" fill="none" stroke="#fff" stroke-width="2"><circle cx="15" cy="15" r="11"/><polyline points="10,15 14,19 21,11"/></svg>
        <h3>No experience needed</h3>
        <p>FlipCrane guides you every step of the way.</p>
        <span class="more">Read more &gt;&gt;</span>
      </div>
      <div class="step">
        <svg viewBox="0 0 30 30" fill="none" stroke="#fff" stroke-width="2"><rect x="5" y="13" width="20" height="14"/><path d="M9 13 V9 a6 6 0 0 1 12 0 V13"/></svg>
        <h3>You are in control</h3>
        <p>You choose and decide where transactions you want to make happen.</p>
        <span class="more">Read more &gt;&gt;</span>
      </div>
      <div class="step">
        <svg viewBox="0 0 30 30" fill="none" stroke="#fff" stroke-width="2"><circle cx="15" cy="15" r="11"/><line x1="7" y1="7" x2="23" y2="23"/></svg>
        <h3>We don't trade Client's Money</h3>
        <p>FlipCrane does not trade for its clients. We provide the best solutions.</p>
        <span class="more">Read more &gt;&gt;</span>
      </div>
    </div>
    <div class="cta"><a class="btn">SUBSCRIBE NOW</a></div>
  </div>
</section>

<section class="section promote">
  <h2 class="title-center">You Want to Promote FlipCrane?</h2>
  <div class="cards">
    <div class="card">
      <div class="card-img" role="img" aria-label="Person shouting through a megaphone" style="background:linear-gradient(135deg,#c9d3da,#8fa3b0)"></div>
      <h3>Spread the word</h3>
      <p>If you have your own blog, website or social channel, tell your audience about us.</p>
      <a class="btn">CONTACT US</a>
    </div>
    <div class="card">
      <div class="card-img" role="img" aria-label="Stack of gold crypto coins" style="background:linear-gradient(135deg,#5b4a2c,#c49a45)"></div>
      <h3>Share and re-link</h3>
      <p>If you have your own video channel, blog or website, add a link to us.</p>
      <a class="btn">CONTACT US</a>
    </div>
    <div class="card">
      <div class="card-img" role="img" aria-label="Laptop showing trading charts" style="background:linear-gradient(135deg,#2d3c52,#6d87a8)"></div>
      <h3>Refer clients and earn</h3>
      <p>Refer new clients to us and receive a share of their paid subscription.</p>
      <a class="btn">CONTACT US</a>
    </div>
  </div>
</section>

<section class="section split">
  <div class="half">
    <div class="photo" role="img" aria-label="Hand holding a smartphone"></div>
    <div class="shade"></div>
    <div class="inner">
      <h2>Jump Capability</h2>
      <ul class="bullets">
        <li>Jump is a special feature that helps you move from one coin to the next with profit.</li>
        <li>Jump to an asset of your choosing with a profitable solution.</li>
        <li>From ANY exchange 2 ANY pair to any asset.</li>
        <li>Our engine can map your trading solutions to an asset that coin in a profitable cost efficient manner.</li>
      </ul>
    </div>
  </div>
  <div class="half right">
    <div class="photo" role="img" aria-label="Smartphone on a desk"></div>
    <div class="shade"></div>
    <div class="inner">
      <h2>We Know What Is Necessary</h2>
      <p>FlipCrane is built by people with 15 years of experience in several asset classes. We worked with top funds and have high degrees of compliance, and industry standards. We also know what it takes to trade and earn.</p>
      <ul class="bullets" style="margin-top:20px">
        <li>Use our combined knowledge to elevate your profits.</li>
      </ul>
    </div>
  </div>
</section>

<section class="section info">
  <div class="email">
    <h2>E-Mail Notification System</h2>
    <p>Pay a fee for better trading solutions that you would use to be notified about. We will send you an email notification when the conditions are met.</p>
    <div class="email-img" role="img" aria-label="Laptop on a desk with a notification screen" style="background:linear-gradient(135deg,#a9b6c2,#dfe4e8)"></div>
  </div>
  <div class="faq">
    <h2>Frequently Asked Questions</h2>
    <ul class="faq-list">
      <li>How to deposit funds?<span class="faq-dot"></span></li>
      <li>Does FlipCrane have a trading Bot?<span class="faq-dot"></span></li>
      <li>Can I pay with cryptocurrency?<span class="faq-dot"></span></li>
      <li class="open">No, at the moment we only use PayNest.</li>
      <li>Can I pay with a credit or debit card?<span class="faq-dot"></span></li>
    </ul>
  </div>
</section>

<footer class="section footer">
  <div><h4>INFO</h4><ul><li>About Us</li><li>Fees</li><li>Promotions</li><li>Coin Metrics</li></ul></div>
  <div><h4>DOCS</h4><ul><li>User Agreement</li><li>Privacy Policy</li><li>API Docs</li></ul></div>
  <div><h4>SUPPORT</h4><ul><li>Contact Us</li><li>FAQ</li></ul></div>
  <div><h4>MEDIA</h4><ul><li>News</li><li>Community</li><li>Press</li></ul></div>
  <div class="meta">Users currently online: 2359<br>FlipCrane 2018. All rights reserved.<br>Design by studio</div>
</footer>

</body>
</html>
```